Business Card Design/Stationary Design

We would like designers to submit cool, hip business card designs (plus stationary designs) for a new, upstart software development company located in Toronto.
If you have any questions, please email us.
For inspiration on designs:
http://cardmuse.example/cool-business-cards/
http://layoutnotes.example/2008/05/36-cool-business-cards-you-should%E2%80%99ve-seen.html
http://gigharbor.example/general/18-smokin-hot-business-card-designs/

Card info:

Selvakumar (Selv) Nadarasan

Founder and CEO

47 Brindle Court, Suite 311

Toronto, ON M4K 2T8

Phone: 647-512-7730

Mobile: 416-273-5094

Fax: 647-512-7731

Email: selvakumar.nadarasan@mailbrook.example

www.quendrix.example
Updates

Hi everyone,

In terms of all the designs I have seen so far, here is what I like:

1.  I really like the "back" part of this design.  The "front" looks pretty decent as well, but for the "front", look at #2 on this list.  I like that.

http://www.pitchboard.example/image.aspx?imageLocation=1000_10001_2000_image.jpg&type=design300px&whiteLabelCustId=9999

2. "Side 1" of this I like, the front needs to be reworked.

http://www.pitchboard.example/image.aspx?imageLocation=1000_10002_2000_image.png&type=design300px&whiteLabelCustId=9999

3. http://www.pitchboard.example/image.aspx?imageLocation=1000_10003_2000_image.jpg&type=design300px&whiteLabelCustId=9999

4. http://www.pitchboard.example/image.aspx?imageLocation=1000_10004_2000_image.jpg&type=design300px&whiteLabelCustId=9999

Target Market(s)

We are focused on enterprise customers right now, so businesses with a long-term goal of also reaching out to the consumer market as well.

Industry/Entity Type

Software

Requirements
Must have
• Must look cool, ultra-modern, clean and eye-catching. Must incorporate our logo and the colors found in the logo.

```html
<!DOCTYPE html>
<html lang="en">
<head>
<meta charset="utf-8">
<title>Quendrix Business Card – Side 1 and Side 2</title>
<link rel="stylesheet" href="https://fonts.googleapis.com/css2?family=Questrial&family=Open+Sans:wght@700&display=swap">
<style>
  :root {
    --page-bg: #ffffff;
    --card-black: #000000;
    --card-white: #ffffff;
    --brand-green: #8dc63f;
    --brand-green-dark: #6aa539;
    --brand-lime: #b5d334;
    --label-green: #7cb342;
    --text-light: #ffffff;
    --shadow: rgba(0, 0, 0, 0.28);
  }
  * { box-sizing: border-box; margin: 0; padding: 0; }
  html, body {
    width: 1200px;
    height: 873px;
    overflow: hidden;
    background: var(--page-bg);
  }
  .sheet {
    position: relative;
    width: 1200px;
    height: 873px;
    font-family: "Questrial", "Century Gothic", sans-serif;
  }
  .side-label {
    position: absolute;
    left: 46px;
    font-family: "Open Sans", Arial, sans-serif;
    font-weight: 700;
    font-size: 58px;
    line-height: 1;
    color: var(--label-green);
    text-shadow: 2px 2px 3px rgba(0, 0, 0, 0.25);
  }
  .side-label--one { top: 158px; }
  .side-label--two { top: 553px; }

  .card {
    position: absolute;
    left: 308px;
    width: 835px;
    height: 403px;
    box-shadow: 3px 4px 8px var(--shadow);
    overflow: hidden;
  }
  .card--front { top: 15px; background: var(--card-black); }
  .card--back { top: 454px; background: var(--card-white); }

  /* Side 1 – centred brand mark */
  .front-brand {
    position: absolute;
    left: 0; right: 0; top: 0; bottom: 0;
    display: flex;
    align-items: center;
    justify-content: center;
    gap: 16px;
  }
  .brand-dot {
    width: 34px;
    height: 34px;
    border-radius: 50%;
    background: var(--brand-green);
  }
  .brand-name {
    color: var(--brand-green);
    font-size: 44px;
    line-height: 1;
  }

  /* Side 2 */
  .back-header {
    position: absolute;
    left: 0; top: 0;
    width: 100%;
    height: 165px;
  }
  .back-brand {
    position: absolute;
    left: 40px;
    top: 54px;
    display: flex;
    align-items: center;
    gap: 14px;
  }
  .back-brand .brand-dot { width: 46px; height: 46px; }
  .back-brand .brand-name { font-size: 56px; }

  .holder {
    position: absolute;
    left: 428px;
    top: 64px;
    width: 400px;
    text-align: left;
  }
  .holder-name {
    color: var(--brand-green);
    font-size: 22px;
    line-height: 1.1;
    white-space: nowrap;
  }
  .holder-title {
    margin-top: 3px;
    color: var(--brand-green-dark);
    font-size: 20px;
    letter-spacing: 1.6px;
    line-height: 1.1;
    margin-left: 4px;
  }

  .rule-top {
    position: absolute;
    left: 0; top: 165px;
    width: 100%; height: 7px;
    background: var(--brand-green);
  }
  .contact-band {
    position: absolute;
    left: 0; top: 172px;
    width: 100%; height: 199px;
    background: var(--card-black);
  }
  .contact-list {
    position: absolute;
    left: 118px;
    top: 16px;
    list-style: none;
  }
  .contact-item {
    display: flex;
    align-items: baseline;
    height: 29px;
    font-size: 17px;
    color: var(--text-light);
    white-space: nowrap;
  }
  .contact-key {
    width: 58px;
    color: var(--brand-green);
  }
  .rule-bottom {
    position: absolute;
    left: 0; top: 377px;
    width: 100%; height: 12px;
    background: var(--brand-green);
  }
</style>
</head>
<body>
<main class="sheet">
  <p class="side-label side-label--one">Side 1</p>
  <section class="card card--front" aria-label="Card front">
    <div class="front-brand">
      <span class="brand-dot"></span>
      <span class="brand-name">Quendrix</span>
    </div>
  </section>

  <p class="side-label side-label--two">Side 2</p>
  <section class="card card--back" aria-label="Card back">
    <header class="back-header">
      <div class="back-brand">
        <span class="brand-dot"></span>
        <span class="brand-name">Quendrix</span>
      </div>
      <div class="holder">
        <p class="holder-name">Selvakumar (Selv) Nadarasan</p>
        <p class="holder-title">FOUNDER AND CEO</p>
      </div>
    </header>
    <div class="rule-top"></div>
    <div class="contact-band">
      <ul class="contact-list">
        <li class="contact-item"><span class="contact-key">p:</span><span>647.512.7730</span></li>
        <li class="contact-item"><span class="contact-key">m:</span><span>416.273.5094</span></li>
        <li class="contact-item"><span class="contact-key">f:</span><span>647.512.7731</span></li>
        <li class="contact-item"><span class="contact-key">w:</span><span>www.quendrix.example</span></li>
        <li class="contact-item"><span class="contact-key">e:</span><span>selvakumar.nadarasan@mailbrook.example</span></li>
        <li class="contact-item"><span class="contact-key">a:</span><span>47 Brindle Court, Suite 311, Toronto, ON M4K 2T8</span></li>
      </ul>
    </div>
    <div class="rule-bottom"></div>
  </section>
</main>
</body>
</html>
```